Brochure for Community-Based Therapy Company

Will be given out to patients, doctors, case managers. We are redesigning our marketing materials and would like a design for a brochure. We provide therapy to individuals who have been injured in car accidents or on the job. We provide occupational therapy, speech therapy and psychotherapy. We would like the brochure to utilize our corporate ID and color scheme that we are using for our other materials (see attached letterhead and logo).

Stock photos that are used should stay away from images of outpatient or hospital settings, stay away from photos with obvious disabilities (wheelchairs, learning to walk, etc), and nothing that looks like physical therapy, as we don't provide physical therapy only OT, Speech and psychotherapy. Would prefer to not have people wearing masks, as we will use this beyond the pandemic. Also, our staff wears business casual clothing so would prefer photos that the individuals are not wearing scrubs or other medical attire (lab coats, etc).

Target Market(s)

Patients, Physicians/Doctors, Case Managers

Industry/Entity Type

Healthcare

Requirements
Must have
• Prefer a booklet format but doesn't have to be 8.5 inch by 11 inch (can be a little smaller).

```html
<!DOCTYPE html>
<html lang="en">
<head>
<meta charset="utf-8">
<title>Northway Therapy Partners – Booklet Spreads</title>
<link rel="stylesheet" href="https://fonts.googleapis.com/css2?family=Roboto:wght@400;500;700&family=Roboto+Condensed:wght@700&display=swap">
<style>
:root{
  --bg:#d6dad2;
  --teal:#5f8b7e;
  --teal-dark:#4b7366;
  --teal-soft:#8fb0a5;
  --paper:#f2f4f4;
  --paper-mist:#e3e8e8;
  --ink:#3d4a47;
  --ink-soft:#6a7773;
  --white:#ffffff;
  --grey-band:#b9bfbf;
}
*{margin:0;padding:0;box-sizing:border-box}
html,body{width:1200px;height:2485px;overflow:hidden;background:var(--bg)}
body{font-family:"Roboto",Arial,sans-serif;color:var(--ink);position:relative}
.spread{position:absolute;left:50px;width:1100px;height:400px;display:flex;box-shadow:0 18px 30px rgba(0,0,0,.12)}
.spread--cover{top:190px}
.spread--intro{top:1040px}
.spread--services{top:1890px}
.page{position:relative;width:550px;height:400px;overflow:hidden;background:var(--paper)}
.page svg.deco{position:absolute;inset:0;width:100%;height:100%}
.photo{position:absolute}
.brand{position:absolute;display:flex;align-items:center;gap:5px;font-weight:700;font-size:11px;letter-spacing:.06em;text-transform:uppercase;color:var(--teal-dark)}
.brand::before{content:"";width:9px;height:9px;border-radius:50%;background:var(--teal-dark)}
.tab{position:absolute;background:var(--teal);color:var(--white);font-family:"Roboto Condensed",sans-serif;font-weight:700;font-size:12px;padding:5px 34px 5px 14px;clip-path:polygon(0 0,100% 0,88% 100%,0 100%);text-transform:uppercase}
.tab--plain{text-transform:none;font-size:12px}
.copy{position:absolute;font-size:7.4px;line-height:1.5;color:var(--ink-soft)}
.copy p{margin-bottom:6px}
.copy b{color:var(--ink)}
.sub{font-family:"Roboto Condensed",sans-serif;font-weight:700;font-size:12px;color:var(--ink);position:absolute;padding-left:10px;border-left:6px solid var(--teal)}
.pagenum{position:absolute;bottom:10px;width:12px;height:12px;background:var(--teal);color:var(--white);font-size:7px;text-align:center;line-height:12px}
.checklist{list-style:none}
.checklist li{padding-left:11px;position:relative;margin-bottom:7px}
.checklist li::before{content:"";position:absolute;left:0;top:2px;width:6px;height:6px;background:var(--teal)}
.dots{list-style:none;padding-left:12px;margin:2px 0 6px}
.dots li::before{content:"• "}
.serve-copy{line-height:1.35}
.serve-copy .checklist li{margin-bottom:5px}
.serve-copy .dots{margin:1px 0 4px}
/* cover */
.pill{position:absolute;background:var(--white);border-radius:14px;font-size:7.5px;color:var(--ink);padding:6px 12px;line-height:1.35}
.contact-line{position:absolute;font-size:7.5px;color:var(--white);line-height:1.5}
.icon{display:inline-block;width:8px;height:8px;border-radius:50%;background:var(--white);margin-right:4px;vertical-align:-1px}
.headline{position:absolute;right:40px;top:50px;color:var(--white);font-size:26px;font-weight:400;text-align:right;line-height:1.15;letter-spacing:.02em}
.headline strong{font-weight:700}
.brand-box{position:absolute;left:170px;bottom:60px;background:var(--white);border-radius:8px;padding:14px 20px;box-shadow:0 3px 8px rgba(0,0,0,.15)}
.brand-box .brand{position:static;font-size:13px}
.heading{position:absolute;font-weight:700;font-size:13px;line-height:1.25;color:var(--teal-dark)}
.page--green{background:var(--teal)}
.page--green .copy{color:#e8f0ed}
</style>
</head>
<body>

<!-- Spread 1: back cover + front cover -->
<section class="spread spread--cover">
  <article class="page page--back">
    <div class="photo" role="img" aria-label="Photo of four friends embracing outdoors at sunset" style="left:0;top:0;width:550px;height:260px;background:linear-gradient(160deg,#c9d3d6 0%,#e7c99a 45%,#b8793e 75%,#6c5a3e 100%)"></div>
    <svg class="deco" viewBox="0 0 550 400" aria-hidden="true">
      <polygon points="0,0 130,0 0,170" fill="#f2f4f4" opacity=".9"/>
      <polygon points="300,0 550,0 550,60 420,40" fill="#5f8b7e"/>
      <polygon points="0,170 60,120 0,200" fill="#e3e8e8"/>
      <polygon points="0,250 550,215 550,400 0,400" fill="#5f8b7e"/>
      <line x1="0" y1="258" x2="550" y2="223" stroke="#8fb0a5" stroke-width="1"/>
      <line x1="220" y1="400" x2="550" y2="330" stroke="#8fb0a5" stroke-width=".8"/>
    </svg>
    <div class="brand" style="left:30px;top:28px">Northway Therapy Partners</div>
    <div class="tab tab--plain" style="left:30px;top:252px;background:#e3e8e8;color:var(--teal-dark);font-size:9px">Contact Us</div>
    <div class="pill" style="left:40px;top:282px"><b>Office Hours:</b><br>Monday – Friday 9:00 am – 4:30 pm</div>
    <div class="pill" style="left:210px;top:282px"><b>Therapy Hours:</b><br>By Appointment</div>
    <div class="contact-line" style="left:40px;top:322px"><span class="icon"></span>1200 Maple Ridge Drive<br>&nbsp;&nbsp;&nbsp;Suite 300, Fairview, MI 48000</div>
    <div class="contact-line" style="left:200px;top:322px"><span class="icon"></span>Office: 555-014-2200<br><span class="icon"></span>Fax: 555-014-2211</div>
    <div class="contact-line" style="right:30px;bottom:22px;text-align:right"><span class="icon"></span>admissions@northway-therapy.com<br><span class="icon"></span>www.northway-therapy.com</div>
  </article>
  <article class="page page--front">
    <div class="photo" role="img" aria-label="Photo of two people holding hands by the water" style="inset:0;background:linear-gradient(120deg,#e8ecee 0%,#e9c9b3 45%,#d8dde0 70%,#c6d0d4 100%)"></div>
    <svg class="deco" viewBox="0 0 550 400" aria-hidden="true">
      <polygon points="0,0 550,90 550,150 0,60" fill="#5f8b7e" opacity=".92"/>
      <polygon points="0,60 90,75 0,400" fill="#5f8b7e" opacity=".55"/>
      <polygon points="0,170 60,230 0,300" fill="#f2f4f4" opacity=".7"/>
      <polygon points="330,400 550,300 550,400" fill="#5f8b7e" opacity=".7"/>
    </svg>
    <h1 class="headline">WE PROVIDE<br>HIGH <strong>QUALITY</strong> THERAPY</h1>
    <div class="brand-box"><div class="brand">Northway Therapy Partners</div></div>
  </article>
</section>

<!-- Spread 2: mission + key factors -->
<section class="spread spread--intro">
  <article class="page">
    <div class="photo" role="img" aria-label="Photo of a clinician with a stethoscope" style="left:180px;top:0;width:370px;height:230px;background:linear-gradient(135deg,#7fcfbd 0%,#4fae9a 50%,#c9a98c 100%);clip-path:polygon(0 0,100% 0,100% 100%,75% 100%)"></div>
    <svg class="deco" viewBox="0 0 550 400" aria-hidden="true">
      <polygon points="270,150 550,260 550,300 300,180" fill="#b9bfbf"/>
      <line x1="0" y1="60" x2="550" y2="20" stroke="#b9bfbf" stroke-width=".8"/>
      <polygon points="160,400 550,330 550,345 200,400" fill="#5f8b7e"/>
    </svg>
    <div class="tab" style="left:0;top:70px">Our Mission</div>
    <div class="copy" style="left:28px;top:110px;width:240px">
      <p><b><i>Mission Statement</i></b> – Our mission is to provide high quality therapy that allows the people we serve to achieve an optimal level of functioning and to improve their quality of life.</p>
      <p><b><i>Vision Statement</i></b> – To be a recognized leader in functional rehabilitation for individuals with a variety of diagnoses in the home and community-based setting, with an emphasis on goal-directed individual rehabilitation for addressing safety, skill building, independence, and cognitive and physical recovery.</p>
    </div>
    <div class="sub" style="left:28px;top:255px">Who We Are</div>
    <div class="copy" style="left:40px;top:282px;width:470px">
      <p>For over 25 years, our company has been using evidence-based principles of rehabilitation to assist patients with their recovery. We are out in the real world with patients every day, helping them to get their lives back. Our goal is to provide functional home and community-based therapy to provide patient-centered holistic therapy with a state-of-the-art approach. Using the patient's natural environment such as their home, community or workplace allows us to attain measurable outcomes that turn even small successes into something bigger.</p>
    </div>
    <div class="pagenum" style="left:24px">3</div>
  </article>
  <article class="page">
    <div class="photo" role="img" aria-label="Photo of a therapist taking notes beside a client at home" style="left:0;top:0;width:150px;height:200px;background:linear-gradient(150deg,#b98c6c 0%,#d9cfc4 50%,#8b8f92 100%);clip-path:polygon(0 0,100% 0,20% 100%,0 100%)"></div>
    <svg class="deco" viewBox="0 0 550 400" aria-hidden="true">
      <polygon points="150,0 170,0 40,220 25,200" fill="#b9bfbf"/>
      <line x1="190" y1="0" x2="20" y2="320" stroke="#b9bfbf" stroke-width=".8"/>
      <polygon points="0,400 550,330 550,345 80,400" fill="#5f8b7e"/>
    </svg>
    <div class="brand" style="right:30px;top:28px">Northway Therapy Partners</div>
    <h2 class="heading" style="left:80px;top:95px;width:380px">Finding success in the rehabilitative process<br>relies on certain key factors:</h2>
    <div class="copy" style="left:90px;top:140px;width:420px">
      <ul class="checklist">
        <li><b>Getting to Know You:</b> We do not set goals that are important to us, but rather, we set goals that are important to you. We take input from you, and the people you trust like your physician, case manager or perhaps a trusted family member to identify your needs and then make a plan that is best suited for success.</li>
        <li><b>Comprehensive Evaluation:</b> We begin with an in-depth assessment with comprehensive evaluation protocols to determine your current level of functioning and how it compares to your prior level of functioning. We can then identify the areas that have been impacted and begin addressing them.</li>
        <li><b>Creating and Implementing a Customized Rehabilitation Plan:</b> After the evaluation protocols are completed, a system of long-term and short-term goals are developed using our team approach. This allows for therapy to be tailored to your individual needs. A plan of care is developed and implemented based on your goals and the results of the evaluation.</li>
        <li><b>Focus on Accomplishments (Breaking Down Success):</b> In order to facilitate progress toward patient goals, our therapy is most effective with consistent therapy appointments and repetition across therapy disciplines, which maximizes carry over outside of therapy.</li>
      </ul>
    </div>
    <div class="pagenum" style="right:24px">4</div>
  </article>
</section>

<!-- Spread 3: approach + who we serve -->
<section class="spread spread--services">
  <article class="page page--green">
    <svg class="deco" viewBox="0 0 550 400" aria-hidden="true">
      <polygon points="0,0 550,0 550,60 0,110" fill="#e3e8e8" opacity=".35"/>
      <line x1="0" y1="330" x2="550" y2="270" stroke="#8fb0a5" stroke-width=".8"/>
      <line x1="0" y1="345" x2="550" y2="290" stroke="#8fb0a5" stroke-width=".5"/>
      <polygon points="390,20 440,20 465,62 440,104 390,104 365,62" fill="#f2f4f4"/>
    </svg>
    <div class="photo" role="img" aria-label="Photo of a hand pointing at brain scan images" style="left:372px;top:26px;width:88px;height:72px;background:linear-gradient(135deg,#2d4a63 0%,#6f8fa8 50%,#d9c3b3 100%);clip-path:polygon(22% 0,78% 0,100% 50%,78% 100%,22% 100%,0 50%)"></div>
    <div class="tab tab--plain" style="left:0;top:80px;background:#f2f4f4;color:var(--teal-dark)">Why Our Approach to Brain Injury is Unique</div>
    <div class="copy" style="left:28px;top:130px;width:490px">
      <p>In more traditional therapy settings such as programs using outpatient models, attempts are made to simulate functional activities combined with more structured tasks, all performed within the clinic environment. However, the inability to generalize learning has been shown to be a reoccurring difficulty for individuals with brain injury and can often manifest in cognitive inflexibility, which makes carryover of their learned skills to the real world a challenge.</p>
      <p>Community-based treatment circumvents this difficulty by conducting therapy in the person's home, school, workplace or other settings within their community, such as a grocery store or at a post office. Clinicians are therefore able to witness first hand where a task is experiencing success or breaking down and can structure treatment accordingly. This allows for greater natural development of functional skills, with generalization issues no longer an obstacle toward meeting treatment goals.</p>
      <p>At our practice we are committed to helping people recover their cognitive, physical and psychosocial abilities following brain injury through intensive individual treatment which focuses on safety, skill building and increasing independence, community reintegration, and overall life satisfaction. Our treatment approach is two fold, with emphasis not only on direct restoration of brain functions, but also on helping the individual learn compensatory strategies such as planners, reminders and organizational systems to reduce the effects of real world disability.</p>
    </div>
    <div class="pagenum" style="left:24px;background:#f2f4f4;color:var(--teal-dark)">5</div>
  </article>
  <article class="page">
    <div class="photo" role="img" aria-label="Photo of a smiling older man in a red sweater" style="left:350px;top:140px;width:200px;height:260px;background:linear-gradient(160deg,#e7c7b5 0%,#d9a58e 55%,#b8202a 85%);clip-path:polygon(40% 0,100% 0,100% 100%,0 100%)"></div>
    <svg class="deco" viewBox="0 0 550 400" aria-hidden="true">
      <polygon points="500,60 520,60 330,340 310,330" fill="#5f8b7e" opacity=".8"/>
      <polygon points="0,0 60,0 0,80" fill="#e3e8e8"/>
      <polygon points="0,400 350,378 350,386 100,400" fill="#5f8b7e"/>
    </svg>
    <div class="brand" style="right:30px;top:28px">Northway Therapy Partners</div>
    <div class="tab tab--plain" style="left:0;top:66px">Who We Serve</div>
    <div class="copy serve-copy" style="left:30px;top:98px;width:330px">
      <ul class="checklist">
        <li>We treat adults and adolescents with a variety of diagnoses. We service home and community locations throughout Southeast and mid Michigan.</li>
        <li>Our therapists hold a variety of certifications and endorsements including CBIS (Certified Brain Injury Specialist), swallowing and voice therapy programs.</li>
      </ul>
      <div style="padding-left:40px">
        <b>Diagnoses can include:</b>
        <ul class="dots">
          <li>Traumatic Brain Injury</li><li>Postconcussional Syndrome</li><li>Spinal Cord Injury</li><li>Post-Traumatic Stress Disorder</li><li>Depression</li><li>Anxiety</li><li>Mood Disorders</li><li>Musculoskeletal/Orthopedic injuries (ie. Spinal fractures/pathology, nerve injuries, pain)</li><li>Visual Impairments</li><li>Balance Disorders</li><li>Movement Disorders</li><li>Neuromuscular Pathologies</li><li>Dysphagia</li>
        </ul>
        <b>Funding Sources include:</b>
        <ul class="dots">
          <li>No-Fault Auto Insurance</li><li>Workers Compensation Insurance</li><li>Some Commercial Health Insurance Carriers</li>
        </ul>
      </div>
    </div>
    <div class="pagenum" style="right:24px">6</div>
  </article>
</section>

</body>
</html>
```